Clean book cover design for book about writing a book

Book title: The Crossing
Subtitle: 9 Paths to Crafting a Volume that Counts
Name: Marisol T. Brenwick, The Quill Nursery

This is a book which teaches 10 steps to writing a self-help book. I'm looking for a very clean impactful cover either with no image or just a small simple image of a book, typewriter, laptop, cabin or something very simple. I am attaching the manuscript here if reading it would help you with the cover. The theme of the book is that you can write with joy and ease and your book can just flow out of you if you learn how to clear the blocks between you and your book already written. Sort of a new agey stance on book writing.

The book should generally match the branding on my website. Www.TheQuillNursery.example.

I have photos of myself attached which I'd like used for the back cover with an "about the author section of maybe 50 words.

The project is for the full back cover and spine as well as the front cover (see print Forge template attached) but to win the contest you can just design the front cover and then I'll give the winner the template for the full design with the back cover copy. Or you can design the full cover using the template and you can use Loren ipsum text if you need to.

My clients are very upmarket and the themes of my business revolve around nuturing and incubating ideas and authors. Very feminine creation energy.

For colors see The Crossing Press (CB) wax seals and the background fades. I don't want my logo on the cover but I am attaching it here so you get a feel for the branding. The logo is in the LOBSTER font and you can see how we do the grey with the rainbow shadow.

Here are some covers I like:

http://www.shopvale.example/Pen-Tome-Quick-Stage---Stage/dp/055817342Q
http://www.shopvale.example/Plotting-Your-Tale-Chart-Triumph/dp/0841739265
http://www.shopvale.example/Be-Scribe-Seeking-Voice-Guide-ebook/dp/K22R9WQ3L1
http://www.shopvale.example/Strays-Tale-Triumph-Rupert-Vanhollow/dp/0552048871
Updates

I have revised my brief to include some picture and images that will help you create the cover. I have also included some of my favorite covers to give you more of a sense of what I'm going for. And I have included the manuscript in case it would help you to skim through it in order to get a sense of the reader and the book. I think if you look at my revised brief it will make it easier to create a submission. Thanks!

Target Market(s)

Women 40-60 who run small businesses as life coaches or other healing jobs (therapy, reiki, light work) they have a spiritual/new age bent.

Industry/Entity Type

Business

Font styles to use
Serif
Other font styles liked:
• Lobster (not required... just a suggestion since it's my logo font)

Requirements
Must have
• Name and title easy to read in 1" x 1" thumb nail
Nice to have
• Fantastic type face treatment.

Match the look and feel of my website.
Should not have
• Busy images. With one simple image or just designed with colors and typeface treatment

```html
<!DOCTYPE html>
<html lang="en">
<head>
<meta charset="utf-8">
<title>The Crossing — Book Cover</title>
<link href="https://fonts.googleapis.com/css2?family=Oswald:wght@400;500&family=Fira+Sans+Condensed:wght@500;700&display=swap" rel="stylesheet">
<style>
  :root {
    --cover-dark: #5e1608;
    --cover-mid: #a4492a;
    --cover-light: #f3cdb0;
    --cover-pale: #fbe6d6;
    --sepia-deep: #6e2c12;
    --sepia-mid: #a9603a;
    --sepia-soft: #d9a07c;
    --sepia-cream: #f8dcc6;
    --gold-top: #ffe56a;
    --gold-mid: #f7c21c;
    --gold-low: #e58a0a;
    --gold-rule: #f4c22a;
    --rule-edge: #8a4a06;
    --subtitle: #ffffff;
    --band-top: #ffb52a;
    --band-low: #f07c06;
    --band-text: #1c0e04;
  }
  html, body {
    margin: 0;
    padding: 0;
    width: 800px;
    height: 1200px;
    overflow: hidden;
    background: #ffffff;
  }
  .cover {
    position: relative;
    width: 800px;
    height: 1200px;
    overflow: hidden;
    background: linear-gradient(180deg,
      var(--cover-dark) 0%,
      #7a2612 18%,
      var(--cover-mid) 34%,
      #c77a55 48%,
      var(--cover-light) 70%,
      var(--cover-pale) 85%,
      #e9b592 100%);
  }
  .artwork {
    position: absolute;
    left: 0;
    top: 430px;
    width: 800px;
    height: 718px;
    background:
      radial-gradient(ellipse 260px 230px at 44% 38%,
        var(--sepia-deep) 0%,
        rgba(110, 44, 18, 0.85) 35%,
        rgba(169, 96, 58, 0.55) 65%,
        rgba(169, 96, 58, 0) 100%),
      radial-gradient(ellipse 520px 420px at 50% 55%,
        var(--sepia-mid) 0%,
        var(--sepia-soft) 55%,
        rgba(248, 220, 198, 0.6) 80%,
        rgba(248, 220, 198, 0) 100%),
      linear-gradient(180deg,
        rgba(199, 122, 85, 0) 0%,
        var(--sepia-cream) 45%,
        #edbf9f 100%);
  }
  .title-rule {
    position: absolute;
    height: 7px;
    background: linear-gradient(180deg, var(--gold-top), var(--gold-rule) 50%, var(--gold-low));
    box-shadow: 0 1px 0 var(--rule-edge);
  }
  .title-rule--left  { left: 40px;  top: 64px; width: 278px; }
  .title-rule--right { left: 490px; top: 64px; width: 275px; }
  .title-rule--base  { left: 38px;  top: 326px; width: 728px; height: 9px; }
  .title {
    position: absolute;
    left: 0;
    top: 0;
    width: 800px;
    margin: 0;
    text-align: center;
    font-family: "Oswald", "Arial Narrow", sans-serif;
    font-weight: 500;
    line-height: 1;
  }
  .title span {
    display: block;
    background: linear-gradient(180deg, var(--gold-top) 0%, var(--gold-mid) 50%, var(--gold-low) 100%);
    -webkit-background-clip: text;
    background-clip: text;
    color: transparent;
    filter: drop-shadow(1px 1px 0 #6b3200) drop-shadow(-1px -1px 0 #6b3200);
  }
  .title__lead {
    font-size: 118px;
    margin-top: 30px;
    letter-spacing: -1px;
  }
  .title__main {
    font-size: 204px;
    margin-top: -72px;
    letter-spacing: -2px;
    transform: scaleX(1.12);
    transform-origin: center;
  }
  .subtitle {
    position: absolute;
    left: 0;
    top: 362px;
    width: 800px;
    margin: 0;
    text-align: center;
    font-family: "Fira Sans Condensed", "Arial Narrow", sans-serif;
    font-weight: 500;
    font-size: 42px;
    color: var(--subtitle);
    text-shadow: 2px 2px 2px #2a0a02, 0 0 3px #2a0a02;
  }
  .author-band {
    position: absolute;
    left: 0;
    bottom: 0;
    width: 800px;
    height: 52px;
    background: linear-gradient(180deg, var(--band-top), var(--band-low));
    display: flex;
    align-items: center;
    justify-content: center;
  }
  .author-band__name {
    margin: 0;
    font-family: "Fira Sans Condensed", "Arial Narrow", sans-serif;
    font-weight: 700;
    font-size: 33px;
    letter-spacing: 1px;
    color: var(--band-text);
  }
</style>
</head>
<body>
  <main class="cover">
    <div class="artwork" role="img" aria-label="Sepia sketch of a hand holding a pen, writing on a sheet of paper"></div>

    <div class="title-rule title-rule--left"></div>
    <div class="title-rule title-rule--right"></div>
    <h1 class="title">
      <span class="title__lead">The</span>
      <span class="title__main">Crossing</span>
    </h1>
    <div class="title-rule title-rule--base"></div>

    <p class="subtitle">9 Paths to Crafting a Volume that Counts</p>

    <footer class="author-band">
      <p class="author-band__name">Marisol T. Brenwick, The Quill Nursery</p>
    </footer>
  </main>
</body>
</html>
```